New Business Card Design Project

Looking for a modern business card design for an import distribution business for industrial technical products. The winning design will translate modern, sophistication, technical, professional and sustainable.

Target Market(s)

Technical customers

Industry/Entity Type

Business

Contact Information for Business Card

Dean Harlow
Sales Manager
M: 0471 625 183
P: 1300 872 619
dean@volkarsystems.com.au
4/18 Galloway Crest Road
Marlow Heights NSW 2159
www.volkarsystems.com.au

Font styles to use
Sans Serif

Colors
ec1f27
606060
000000
fbfbfb

Requirements
Must have
• My Logo which is the Volkar Systems logo attached
Nice to have
• Eurostile Bold font

```html
<!DOCTYPE html>
<html lang="en">
<head>
<meta charset="utf-8">
<title>Volkar Systems – Business Card</title>
<link rel="stylesheet" href="https://fonts.googleapis.com/css2?family=Exo+2:wght@400;600;700&family=Michroma&display=swap">
<style>
  :root {
    --red: #ec1f27;
    --slate: #606060;
    --slate-deep: #55595f;
    --black: #000000;
    --paper: #fbfbfb;
    --stage: #2b2b2d;
    --contact: #eaeaea;
  }
  * { box-sizing: border-box; margin: 0; padding: 0; }
  html, body { width: 1200px; height: 997px; overflow: hidden; }
  body {
    background: var(--stage);
    font-family: "Exo 2", Arial, sans-serif;
    position: relative;
  }
  .card {
    position: absolute;
    width: 525px;
    height: 300px;
    border-radius: 16px;
    overflow: hidden;
  }

  /* Card back */
  .card-back {
    left: 50px;
    top: 150px;
    background: linear-gradient(160deg, #6a6e74 0%, var(--slate-deep) 100%);
    display: flex;
    align-items: center;
    justify-content: center;
  }
  .brand {
    display: flex;
    align-items: center;
    gap: 14px;
    white-space: nowrap;
  }
  .brand-square {
    width: 34px;
    height: 34px;
    background: var(--red);
    flex: none;
  }
  .brand-name {
    font-family: "Michroma", "Exo 2", sans-serif;
    color: var(--red);
    font-size: 28px;
    letter-spacing: 1px;
    line-height: 1;
  }

  /* Card front */
  .card-front {
    left: 625px;
    top: 480px;
    background: var(--slate-deep);
  }
  .front-panel {
    position: absolute;
    left: 18px; top: 0; bottom: 0;
    width: 300px;
    background: var(--paper);
    clip-path: polygon(0 0, 270px 0, 300px 100%, 0 100%);
  }
  .front-panel .brand {
    position: absolute;
    left: 20px;
    top: 105px;
    gap: 9px;
  }
  .front-panel .brand-square { width: 24px; height: 24px; }
  .front-panel .brand-name { font-size: 15px; letter-spacing: 0.5px; }
  .web {
    position: absolute;
    left: 22px;
    bottom: 40px;
    font-size: 15px;
    letter-spacing: 1px;
    color: var(--slate);
    white-space: nowrap;
  }
  .web .web-domain { color: var(--red); }

  .identity {
    position: absolute;
    right: 26px;
    top: 24px;
    text-align: right;
    color: var(--paper);
  }
  .identity .person {
    font-weight: 600;
    font-size: 16px;
    letter-spacing: 0.5px;
  }
  .identity .role {
    font-size: 11px;
    color: #e6e6e6;
    margin-top: 2px;
  }
  .contacts {
    position: absolute;
    left: 332px;
    top: 116px;
    list-style: none;
    color: var(--contact);
    font-size: 12px;
    line-height: 19px;
    white-space: nowrap;
  }
  .contacts li { display: flex; align-items: flex-start; gap: 7px; }
  .contacts svg { width: 10px; height: 10px; margin-top: 4px; flex: none; fill: var(--black); }
  .contacts .indent { padding-left: 17px; }
</style>
</head>
<body>

  <section class="card card-back" aria-label="Card back">
    <div class="brand">
      <span class="brand-square"></span>
      <span class="brand-name">VOLKAR SYSTEMS</span>
    </div>
  </section>

  <section class="card card-front" aria-label="Card front">
    <div class="front-panel">
      <div class="brand">
        <span class="brand-square"></span>
        <span class="brand-name">VOLKAR SYSTEMS</span>
      </div>
      <p class="web">www.<span class="web-domain">volkarsystems</span>.com.au</p>
    </div>

    <div class="identity">
      <p class="person">Dean Harlow</p>
      <p class="role">Sales Manager</p>
    </div>

    <ul class="contacts">
      <li>
        <svg viewBox="0 0 10 10" aria-hidden="true"><path d="M2 0.5 L3.5 0.5 L4.2 3 L3 4 Q4 6 6 7 L7 5.8 L9.5 6.5 L9.5 8 Q9.5 9.5 8 9.5 Q1 8.5 0.5 2 Q0.5 0.5 2 0.5Z"/></svg>
        <span>0471 625 183</span>
      </li>
      <li>
        <svg viewBox="0 0 10 10" aria-hidden="true"><rect x="2.5" y="0.5" width="5" height="3"/><rect x="0.5" y="3.5" width="9" height="4" rx="1"/><rect x="2.5" y="6.5" width="5" height="3"/></svg>
        <span>1300 872 619</span>
      </li>
      <li>
        <svg viewBox="0 0 10 10" aria-hidden="true"><rect x="0.5" y="2" width="9" height="6.5"/><path d="M0.5 2 L5 5.5 L9.5 2" stroke="#eaeaea" stroke-width="0.8" fill="none"/></svg>
        <span>dean@volkarsystems.com.au</span>
      </li>
      <li>
        <svg viewBox="0 0 10 10" aria-hidden="true"><path d="M5 0.5 Q8.5 0.5 8.5 4 Q8.5 6 5 9.5 Q1.5 6 1.5 4 Q1.5 0.5 5 0.5Z"/><circle cx="5" cy="4" r="1.3" fill="#eaeaea"/></svg>
        <span>4/18 Galloway Crest Road,</span>
      </li>
      <li class="indent"><span>Marlow Heights NSW 2159</span></li>
    </ul>
  </section>

</body>
</html>
```